依頼概要
■依頼の目的/概要
インフルエンザワクチンのポスターを作成して頂きたいです。
クリニック内の待合室に掲示します。

■依頼詳細
A2サイズです。
温かみのある柔らかいデザインをお願いします。
ポスターには、人のイラスト入りでお願いします。イラストはご自身で書いてくださってもいいですし、フリー素材でも構いません。
色合いは当院ホームページを参考にしてください。
当院ホームページ https://temuzeku.com/

記載する内容については、添付ファイルを参照してください。
ロゴデータは当選決定後に送らせて頂きます。

納品は、元データ(aiファイルやpsdファイル)とPNG書き出しでお願いします。

■重視する点
過去・現在までにデザインの経験のある方を希望致します。

その他何かご不明な点がございましたら、お気軽にご質問下さい。
よろしくお願いいたします。

文字が大きく読みやすい、温かみのあるデザインです。

皆さま、この度は当コンペにご参加いただき、誠にありがとうございます。
どれも力作で魅力的で選ぶのが大変でした。
今後ともどうぞよろしくお願いします。

```html
<!DOCTYPE html>
<html lang="ja">
<head>
<meta charset="UTF-8">
<title>インフルエンザワクチン予防接種</title>
<link rel="stylesheet" href="https://fonts.googleapis.com/css2?family=M+PLUS+Rounded+1c:wght@500;700;800;900&display=swap">
<style>
  :root {
    --green: #7fb13a;
    --green-dark: #3f7a24;
    --green-pale: #e8f1d2;
    --cream: #fbf7e4;
    --red: #d8365a;
    --blue: #3b8fc7;
    --blue-pale: #e3f0f8;
    --ink: #3a3a3a;
    --white: #ffffff;
  }
  * { margin: 0; padding: 0; box-sizing: border-box; }
  html, body { width: 851px; height: 1200px; overflow: hidden; }
  body {
    font-family: "M PLUS Rounded 1c", sans-serif;
    background: var(--cream);
    color: var(--ink);
  }
  .poster { position: relative; width: 851px; height: 1200px; overflow: hidden; }

  .headline {
    background: var(--green);
    height: 222px;
    text-align: center;
    padding-top: 20px;
  }
  .headline-top, .headline-main {
    font-size: 80px; font-weight: 900; color: var(--white);
    letter-spacing: 4px; line-height: 1;
    text-shadow: 3px 3px 0 var(--green-dark);
  }
  .headline-row {
    display: flex; justify-content: center; align-items: center;
    gap: 14px; margin-top: 18px;
  }
  .vaccine-pill {
    background: var(--white); color: var(--green-dark);
    font-size: 38px; font-weight: 900;
    padding: 6px 20px; border-radius: 40px; line-height: 1.1;
  }

  .notice { text-align: center; margin-top: 18px; }
  .start-date { font-size: 44px; font-weight: 900; color: var(--red); line-height: 1.2; }
  .target { font-size: 40px; font-weight: 900; color: var(--green-dark); line-height: 1.3; }
  .no-booking {
    display: inline-block; margin-top: 8px;
    background: var(--red); color: var(--white);
    font-size: 30px; font-weight: 800;
    padding: 4px 34px; border-radius: 30px;
  }

  .people-art {
    position: absolute; left: 70px; top: 418px; width: 711px; height: 208px;
    background: linear-gradient(180deg, #f4e3c5 0%, #f0cda5 55%, #9ec07a 100%);
    border-radius: 110px 110px 0 0;
  }

  .info-panel {
    position: absolute; left: 22px; top: 626px; width: 807px; height: 540px;
    background: var(--green-pale);
    border-radius: 22px;
    padding: 24px 32px;
  }
  .info-title {
    text-align: center; color: var(--red);
    font-size: 32px; font-weight: 900; line-height: 1.2;
  }
  .info-list { list-style: none; margin-top: 14px; }
  .info-list li {
    font-size: 18px; font-weight: 700; line-height: 1.55;
    padding-left: 22px; position: relative;
  }
  .info-list li::before {
    content: ""; position: absolute; left: 2px; top: 8px;
    border-left: 12px solid var(--green-dark);
    border-top: 7px solid transparent; border-bottom: 7px solid transparent;
  }

  .fee-boxes { display: flex; gap: 20px; margin-top: 20px; align-items: flex-start; }
  .fee-box { background: var(--white); border-radius: 8px; overflow: hidden; }
  .fee-box--senior { width: 375px; border: 3px solid var(--green); }
  .fee-side { width: 348px; display: flex; flex-direction: column; }
  .fee-box--adult { border: 3px solid var(--blue); }
  .fee-head {
    color: var(--white); text-align: center;
    font-size: 20px; font-weight: 800; padding: 6px 0;
  }
  .fee-box--senior .fee-head { background: var(--green); }
  .fee-box--adult .fee-head { background: var(--blue); }
  .fee-sub {
    text-align: center; font-size: 17px; font-weight: 800;
    background: var(--green-pale); padding: 5px 0;
    color: var(--green-dark);
  }
  .fee-note { font-size: 12px; line-height: 1.5; padding: 8px 12px; border-bottom: 1px dashed var(--green); }
  .fee-lines { list-style: none; padding: 10px 14px 12px; }
  .fee-lines li { font-size: 14px; font-weight: 700; line-height: 1.7; }
  .fee-box--adult .fee-lines { background: var(--blue-pale); }

  .clinic { margin-top: 130px; padding-left: 70px; }
  .clinic-dept { font-size: 10px; font-weight: 500; color: var(--ink); }
  .clinic-name {
    font-size: 28px; font-weight: 800; color: var(--green-dark); line-height: 1.2;
  }
</style>
</head>
<body>
<main class="poster">
  <header class="headline">
    <div class="headline-top">インフルエンザ</div>
    <div class="headline-row">
      <span class="vaccine-pill">ワクチン</span>
      <span class="headline-main">予防接種</span>
    </div>
  </header>

  <section class="notice">
    <p class="start-date">10月11日(金)からはじまります!</p>
    <p class="target">中学生(13歳)以上の方が対象です。</p>
    <p class="no-booking">予約の必要ありません。</p>
  </section>

  <div class="people-art" role="img" aria-label="笑顔の家族や世代の異なる人々が並ぶイラスト"></div>

  <section class="info-panel">
    <h2 class="info-title">予防と重症化を防ぐため、ワクチンの接種を!!</h2>
    <ul class="info-list">
      <li>インフルエンザに対する抵抗力がつくまで約２週間かかり、その効果は約３～５ヵ月間持続します。</li>
      <li>２回接種をご希望の方は、１回目接種から４週間後に２回目接種を行います。</li>
      <li>肺炎球菌ワクチンや他のワクチンとの同時接種はできます。</li>
      <li>体温が３７.５度以上、具合が悪い方は別の日に接種しましょう。</li>
    </ul>

    <div class="fee-boxes">
      <div class="fee-box fee-box--senior">
        <div class="fee-head">６５歳以上の方</div>
        <div class="fee-sub">60歳以上65歳未満の方</div>
        <p class="fee-note">心臓・腎臓・肺などに障害のある方も対象となります。<br>※詳しくは受付までお問い合わせ下さい</p>
        <ul class="fee-lines">
          <li>■緑ヶ丘市公費負担あり</li>
          <li>■接種費用　¥1,500</li>
          <li>■期　間　10月1日～令和01年12月31日</li>
          <li>※費用が免除になる方がいらっしゃいます。</li>
        </ul>
      </div>
      <div class="fee-side">
        <div class="fee-box fee-box--adult">
          <div class="fee-head">13歳以上65歳未満の方</div>
          <ul class="fee-lines">
            <li>■接種費用　¥4,000/1回目・¥3,000/2回目</li>
            <li>■期　間　10月1日～</li>
          </ul>
        </div>
        <footer class="clinic">
          <p class="clinic-dept">内科・呼吸器内科・循環器内科・消化器内科</p>
          <p class="clinic-name">森川内科クリニック</p>
        </footer>
      </div>
    </div>
  </section>
</main>
</body>
</html>
```